Tovek - Business Card Design

Design a modern masculine business card for our business

Target Market(s)

Private Market

Industry/Entity Type

Construction

Contact Information for Business Card

Company Name - Name of Person - Address - email address - contact number

Font styles to use
Serif
Sans Serif

Colors
0094D4
00A9DD
6FCCEA
C7EBF8
E9F6FB
00AB8E
00BBA5
67D7C9
C6EFE9
E9F9F6
F0912C
F2A743
F7CA91
FBE8D2
FDF5EE

Requirements
Must have
• Use company logo provided
Nice to have
• Company Logo

```html
<!DOCTYPE html>
<html lang="en">
<head>
<meta charset="utf-8">
<title>Tovek Construction – Business Card</title>
<link rel="stylesheet" href="https://fonts.googleapis.com/css2?family=Montserrat:wght@400;500;800&family=Noto+Serif:wght@700&display=swap">
<style>
  :root {
    --stage: #474747;
    --card: #ffffff;
    --ink: #1a1a1a;
    --orange: #f0732c;
    --text: #2a2a2a;
  }
  * { margin: 0; padding: 0; box-sizing: border-box; }
  html, body { width: 1200px; height: 801px; overflow: hidden; }
  body {
    background: var(--stage);
    font-family: "Montserrat", sans-serif;
    position: relative;
  }
  .card {
    position: absolute;
    top: 246px;
    width: 540px;
    height: 309px;
    background: var(--card);
    overflow: hidden;
    box-shadow: 0 12px 30px rgba(0,0,0,.35);
  }
  .card--front { left: 40px; }
  .card--back { left: 620px; border-bottom: 3px solid var(--orange); }
  .card__wave { position: absolute; inset: 0; }

  .wordmark {
    position: absolute;
    display: flex;
    align-items: center;
    gap: 10px;
    color: var(--ink);
    font-family: "Montserrat", sans-serif;
    font-weight: 800;
    text-transform: uppercase;
    line-height: 1.15;
  }
  .wordmark__square { background: var(--orange); flex: none; }
  .card--front .wordmark {
    left: 30px; top: 132px; width: 200px; font-size: 18px;
  }
  .card--front .wordmark__square { width: 14px; height: 14px; }
  .card--back .wordmark {
    left: 0; right: 0; top: 136px; justify-content: center;
    font-size: 26px; gap: 14px; white-space: nowrap;
  }
  .card--back .wordmark__square { width: 20px; height: 20px; }

  .divider {
    position: absolute;
    left: 250px; top: 38px;
    width: 1.5px; height: 136px;
    background: var(--orange);
  }
  .contact {
    position: absolute;
    left: 266px; top: 36px;
    color: var(--text);
    font-size: 11px;
    line-height: 1.4;
  }
  .contact__name {
    font-family: "Noto Serif", serif;
    font-weight: 700;
    color: var(--orange);
    font-size: 16px;
    letter-spacing: .3px;
    line-height: 1.1;
  }
  .contact__role { margin-bottom: 9px; }
  .contact__address { margin-bottom: 9px; }
  .contact__row { display: flex; align-items: center; gap: 6px; }
  .contact__icon { width: 10px; height: 10px; flex: none; }
</style>
</head>
<body>

<section class="card card--front" aria-label="Business card front">
  <svg class="card__wave" viewBox="0 0 540 309" aria-hidden="true">
    <path d="M66 309 C112 262 220 248 540 206 L540 309 Z" fill="var(--orange)"/>
    <path d="M44 309 C92 250 200 234 540 190" fill="none" stroke="var(--ink)" stroke-width="5"/>
  </svg>

  <div class="wordmark"><span class="wordmark__square"></span><span>Tovek Construction, Inc</span></div>

  <div class="divider"></div>

  <div class="contact">
    <p class="contact__name">DANIEL REYES</p>
    <p class="contact__role">Managing Director</p>
    <p class="contact__address">Your address, City<br>State, Zip 1234</p>
    <p class="contact__row">
      <svg class="contact__icon" viewBox="0 0 10 10" aria-hidden="true"><path d="M2 1 L4 1 L4.6 3 L3.4 3.8 Q4.4 5.8 6.2 6.6 L7 5.4 L9 6 L9 8 Q9 9 8 9 Q1 8.4 1 2 Q1 1 2 1 Z" fill="var(--orange)"/></svg>
      123 456 789
    </p>
    <p class="contact__row">
      <svg class="contact__icon" viewBox="0 0 10 10" aria-hidden="true"><rect x="0.5" y="2" width="9" height="6" rx="0.8" fill="var(--orange)"/><path d="M0.8 2.4 L5 5.4 L9.2 2.4" fill="none" stroke="#fff" stroke-width="0.9"/></svg>
      info@yourgmail.com
    </p>
    <p class="contact__row">
      <svg class="contact__icon" viewBox="0 0 10 10" aria-hidden="true"><circle cx="5" cy="5" r="4.5" fill="var(--orange)"/><path d="M0.5 5 H9.5 M5 0.5 Q2.5 5 5 9.5 M5 0.5 Q7.5 5 5 9.5" fill="none" stroke="#fff" stroke-width="0.7"/></svg>
      www.yourwebsite.com
    </p>
  </div>
</section>

<section class="card card--back" aria-label="Business card back">
  <div class="wordmark"><span class="wordmark__square"></span><span>Tovek Construction, Inc</span></div>
</section>

</body>
</html>
```